business card for LWR pty ltd

We require a business card that stands out . I have included our company flyer and would like the services listed to be put on the card so when we Give out the cards to customers they have an idea of services we provide. need the winning design to be in editable photo shop format, editable iMac pages format or editable windows publisher format, so that I can enter in names, email addresses, phone numbers etc myself. I have included a pdf documents of info / items needed on the card to use as reference please.
Updates

need more submissions

Need extra days to review

Sick

Target Market(s)

new customers

Contact Information for Business Card

details are on attached business card requirements file

Requirements
Must have
• I have attached a list of must haves

```html
<!DOCTYPE html>
<html lang="en">
<head>
<meta charset="utf-8">
<title>LWR pty ltd – Business Card</title>
<link href="https://fonts.googleapis.com/css2?family=Lato:wght@300;400;700&family=Montserrat:wght@700&display=swap" rel="stylesheet">
<style>
  :root {
    --page: #ffffff;
    --card-black: #050505;
    --ink-white: #f2f2f2;
    --ink-grey: #c9c9c9;
    --silver: #d8d8d8;
    --gold: #b8925a;
    --tab-grey: #6d6d6d;
    --dirt: #b9784a;
    --dirt-dark: #7a4a2c;
    --sky: #9fb6c9;
  }
  * { box-sizing: border-box; margin: 0; padding: 0; }
  html, body { width: 1200px; height: 1200px; overflow: hidden; background: var(--page); }
  .canvas {
    position: relative; width: 1200px; height: 1200px;
    display: flex; flex-direction: column; align-items: center; justify-content: center; gap: 24px;
  }
  .card {
    position: relative; width: 880px; height: 538px;
    background: var(--card-black); border-radius: 22px; overflow: hidden;
    box-shadow: 0 10px 28px rgba(0,0,0,.22);
    font-family: "Lato", sans-serif; color: var(--ink-white);
  }

  /* ---------- Front ---------- */
  .front-wordmark {
    position: absolute; left: 470px; top: 160px; width: 340px; text-align: center;
    font-family: "Lato", sans-serif; font-weight: 700; font-size: 96px; letter-spacing: 4px;
    line-height: 1; color: var(--silver);
  }
  .front-details { position: absolute; left: 62px; top: 270px; }
  .person-name {
    font-family: "Montserrat", sans-serif; font-weight: 700; font-size: 27px;
    letter-spacing: 3px; color: var(--ink-grey); text-transform: uppercase;
  }
  .person-role { font-weight: 300; font-size: 22px; margin-top: 2px; }
  .address { font-weight: 300; font-size: 22px; line-height: 1.25; margin-top: 24px; }
  .contact-list { list-style: none; margin-top: 22px; }
  .contact-list li {
    display: flex; align-items: center; gap: 12px;
    font-weight: 300; font-size: 22px; line-height: 1.3;
  }
  .contact-list svg { width: 16px; height: 16px; flex: none; }

  /* ---------- Back ---------- */
  .photo { position: absolute; }
  .photo-roadtrain {
    left: 300px; top: 0; width: 580px; height: 320px;
    background: linear-gradient(180deg, #0b0b0b 0%, #1a1a1a 45%, #3a3836 60%, var(--dirt) 78%, var(--dirt-dark) 100%);
  }
  .mesh-band {
    left: 0; top: 0; width: 560px; height: 200px;
    background: linear-gradient(180deg, #1e1e1e 0%, #0c0c0c 100%);
    -webkit-mask: linear-gradient(90deg, #000 70%, transparent 100%);
            mask: linear-gradient(90deg, #000 70%, transparent 100%);
  }
  .photo-lead-truck {
    left: 0; top: 195px; width: 440px; height: 140px;
    background: linear-gradient(180deg, #262626 0%, #4b433c 50%, var(--dirt) 100%);
  }
  .photo-lowloader {
    left: 0; top: 335px; width: 420px; height: 203px;
    background: linear-gradient(180deg, var(--sky) 0%, #c9d1d6 30%, #8d8f8c 55%, #4c4a46 100%);
    clip-path: polygon(0 0, 100% 0, 88% 100%, 0 100%);
  }
  .photo-right-trucks {
    left: 650px; top: 335px; width: 230px; height: 203px;
    background: linear-gradient(160deg, #0d0d0d 0%, #3b3733 40%, #8a7a62 70%, #2a2622 100%);
    clip-path: polygon(14% 0, 100% 0, 100% 100%, 0 100%);
  }
  .back-wordmark {
    position: absolute; left: 200px; top: 70px;
    font-family: "Lato", sans-serif; font-weight: 700; font-size: 104px; letter-spacing: 6px;
    line-height: 1; color: var(--silver);
  }
  .dividers { position: absolute; inset: 0; width: 880px; height: 538px; }
  .services {
    position: absolute; left: 400px; top: 330px; width: 250px; height: 208px;
  }
  .services-tab {
    position: absolute; left: 88px; top: 0; width: 150px; height: 30px;
    background: var(--tab-grey); clip-path: polygon(0 0, 100% 0, 92% 100%, 8% 100%);
    color: var(--ink-white); font-weight: 700; font-size: 16px;
    display: flex; align-items: center; justify-content: center;
  }
  .services-list { list-style: none; position: absolute; left: 28px; top: 38px; }
  .services-list li {
    position: relative; padding-left: 16px; font-size: 11.5px; line-height: 12.8px; color: var(--ink-white);
  }
  .services-list li::before {
    content: ""; position: absolute; left: 0; top: 3px; width: 7px; height: 7px;
    border-radius: 50%; background: var(--gold);
  }
</style>
</head>
<body>
<main class="canvas">

  <section class="card card-front">
    <div class="front-wordmark">LWR</div>

    <div class="front-details">
      <h1 class="person-name">Daniel Hart</h1>
      <p class="person-role">Director</p>
      <p class="address">Lot 444 example<br>address Australia</p>
      <ul class="contact-list">
        <li>
          <svg viewBox="0 0 16 16"><circle cx="8" cy="8" r="8" fill="#f2f2f2"/><path d="M5 4.5c.6-.5 1.2-.4 1.5.2l.6 1.2c.2.4 0 .8-.3 1l-.4.3c.4.9 1.1 1.6 2 2l.3-.4c.2-.3.6-.5 1-.3l1.2.6c.6.3.7.9.2 1.5-.7.8-1.7.9-2.7.4-1.600-.8-2.8-2-3.6-3.6-.5-1-.4-2 .2-2.9z" fill="#050505"/></svg>
          000 444 000
        </li>
        <li>
          <svg viewBox="0 0 16 16"><rect x="1" y="3.5" width="14" height="9" fill="#f2f2f2"/><path d="M1 3.5l7 5 7-5" fill="none" stroke="#050505" stroke-width="1.2"/></svg>
          email@lwrservices.com.au
        </li>
        <li>
          <svg viewBox="0 0 16 16"><circle cx="8" cy="8" r="7.5" fill="#f2f2f2"/><path d="M.5 8h15M8 .5c-3 3.5-3 11.5 0 15M8 .5c3 3.5 3 11.5 0 15" fill="none" stroke="#050505" stroke-width="1"/></svg>
          www.lwrhaulage.com.au
        </li>
      </ul>
    </div>
  </section>

  <section class="card card-back">
    <div class="photo photo-roadtrain" role="img" aria-label="Photo of tipper road trains parked on red outback dirt at dusk"></div>
    <div class="photo mesh-band" role="img" aria-label="Dark metal mesh backdrop behind the company name"></div>
    <div class="back-wordmark">LWR</div>
    <div class="photo photo-lead-truck" role="img" aria-label="Photo of a prime mover pulling tipper trailers on a dirt road"></div>
    <div class="photo photo-lowloader" role="img" aria-label="Photo of a white prime mover hauling a grader on a drop deck trailer"></div>
    <div class="photo photo-right-trucks" role="img" aria-label="Photo of two road train prime movers side by side"></div>

    <svg class="dividers" viewBox="0 0 880 538" aria-hidden="true">
      <path d="M420 335 L396 538" stroke="#b8925a" stroke-width="4"/>
      <path d="M682 335 L650 538" stroke="#b8925a" stroke-width="4"/>
      <path d="M0 335 H880" stroke="#050505" stroke-width="2"/>
    </svg>

    <div class="services">
      <div class="services-tab">Our Services</div>
      <ul class="services-list">
        <li>Over size loads/Hot Shot Loads</li>
        <li>Heavy Vehicle Recovery Services</li>
        <li>Potable Water Deliveries</li>
        <li>Road building/Maintenance</li>
        <li>Earthworks</li>
        <li>Sand &amp; Metal Supply &amp; Cartage</li>
        <li>Road Train Tippers</li>
        <li>Road Train Tankers</li>
        <li>Road Train Flat Tops</li>
        <li>Drop Deck Trailers</li>
        <li>Mine Site accredited</li>
        <li>Equipment &amp; Operator</li>
      </ul>
    </div>
  </section>

</main>
</body>
</html>
```